Manufacturing Company Business card

K & T is a leading supplier of complex machine parts, assemblies and sub assemblies to the aerospace industry.
we would like to create a new feel for our manufacturing company business card design.
We are into lean manufacturing, bold design, metal, use current logo, use "this is your life" logo for entire back of card. updated look for 2015, text, bardcode, etc

our primary end use is flight control components used on about all commercial and business jets in use as well as military aircraft and civil aviation.

Reason: Need more time to review with internal team at KTmfg:)

Target Market(s)

aerospace, manufacturing

Industry/Entity Type

Aero

Contact Information for Business Card

New, industrial, trendy, use current logo, we like text, vmail is lame :( cell ph is ok - what is a fax???

Font styles to use
Serif
Sans Serif

Requirements
Must have
• incorporate our current logo, one option is an Industrial look, metal etc. we can also try to incorporate the feel of the back of the card onto the front but not so busy.
• Back of card full size "this is your life"
• front side, barcode, cell, - our motto "solutions in manufacturing" tm
Nice to have
• Professional look
• up to date
• appeals to broad audience
Should not have
• too much content - pictures of planes

```html
<!DOCTYPE html>
<html lang="en">
<head>
<meta charset="utf-8">
<title>K &amp; T Manufacturing – Business Card</title>
<link rel="stylesheet" href="https://fonts.googleapis.com/css2?family=Open+Sans:wght@400;600;700&display=swap">
<style>
  :root {
    --backdrop: #33454c;
    --card-white: #ffffff;
    --ink-black: #141414;
    --brand-green: #129a4e;
    --ring-grey: #c9c9c9;
    --contact-white: #f2f2f2;
  }
  * { margin: 0; padding: 0; box-sizing: border-box; }
  html, body {
    width: 1200px; height: 900px; overflow: hidden;
    background: var(--backdrop);
    font-family: "Open Sans", Arial, sans-serif;
  }
  .canvas {
    width: 1200px; height: 900px;
    display: flex; flex-direction: column; align-items: center; justify-content: center;
    gap: 60px;
  }
  .card {
    position: relative;
    width: 620px; height: 360px;
    border-radius: 18px;
    overflow: hidden;
    background: var(--card-white);
  }
  .card-shapes { position: absolute; inset: 0; }
  .wordmark {
    position: absolute;
    display: flex; align-items: center; gap: 10px;
    color: var(--ink-black);
    font-weight: 700;
    letter-spacing: 0.5px;
    white-space: nowrap;
  }
  .wordmark-ring {
    border: 2px solid var(--ring-grey);
    border-radius: 50%;
    flex: none;
  }
  .front .wordmark { top: 44px; left: 300px; font-size: 20px; }
  .front .wordmark-ring { width: 40px; height: 40px; }
  .back .wordmark {
    top: 50%; left: 50%; transform: translate(-50%, -50%);
    font-size: 34px; gap: 16px;
  }
  .back .wordmark-ring { width: 74px; height: 74px; }
  .holder {
    position: absolute; right: 58px; top: 118px; text-align: right;
  }
  .holder-name { font-size: 23px; font-weight: 700; color: var(--ink-black); line-height: 1.2; }
  .holder-role { font-size: 14px; font-weight: 400; color: var(--brand-green); }
  .contacts {
    position: absolute; left: 28px; top: 178px;
    list-style: none;
  }
  .contacts li {
    display: flex; align-items: center; gap: 12px;
    color: var(--contact-white);
    font-size: 15px; line-height: 19px;
  }
  .contacts svg { width: 15px; height: 15px; flex: none; }
</style>
</head>
<body>
<main class="canvas">

  <section class="card front" aria-label="Business card front">
    <svg class="card-shapes" viewBox="0 0 620 360" preserveAspectRatio="none" aria-hidden="true">
      <path d="M0,30 C210,150 420,235 620,172 L620,360 L0,360 Z" fill="var(--brand-green)"/>
      <path d="M0,30 C200,155 400,262 620,205 L620,360 L0,360 Z" fill="var(--ink-black)"/>
    </svg>

    <div class="wordmark"><span class="wordmark-ring"></span>K &amp; T MANUFACTURING</div>

    <div class="holder">
      <p class="holder-name">Marc Dalton</p>
      <p class="holder-role">Owner</p>
    </div>

    <ul class="contacts">
      <li>
        <svg viewBox="0 0 16 16" aria-hidden="true"><rect x="4" y="1" width="8" height="14" rx="1.5" fill="none" stroke="var(--brand-green)" stroke-width="1.5"/><circle cx="8" cy="12.5" r="0.9" fill="var(--brand-green)"/></svg>
        +33 410 552 617
      </li>
      <li>
        <svg viewBox="0 0 16 16" aria-hidden="true"><path d="M4,1.5 L6.5,4.5 L5,6.5 C6,8.5 7.5,10 9.5,11 L11.5,9.5 L14.5,12 L13,14.5 C7,14 2,9 1.5,3 Z" fill="var(--brand-green)"/></svg>
        +33-4100-5526
      </li>
      <li>
        <svg viewBox="0 0 16 16" aria-hidden="true"><rect x="4" y="1.5" width="8" height="4" fill="var(--brand-green)"/><rect x="1" y="6" width="14" height="6" rx="1.5" fill="var(--brand-green)"/><rect x="4" y="10.5" width="8" height="4" fill="var(--brand-green)"/></svg>
        +33 4187 3390
      </li>
    </ul>
  </section>

  <section class="card back" aria-label="Business card back">
    <div class="wordmark"><span class="wordmark-ring"></span>K &amp; T MANUFACTURING</div>
  </section>

</main>
</body>
</html>
```